New Business Card Design Project

Use the flyer uploaded and website www.brightoakbuilders.com for inspiration.
List Our Services on Backside of business cards
Martin Hollis
Harborline Renovations Inc.
Licensed General Contractors
858-471-9063

Contact Information for Business Card

Use the flyer uploaded and website www.brightoakbuilders.com for inspiration. List Our Services on Backside of business cards Martin Hollis Harborline Renovations Inc. Licensed General Contractors 858-471-9063

```html
<!DOCTYPE html>
<html lang="en">
<head>
<meta charset="utf-8">
<title>Harborline Renovations – Business Cards</title>
<link href="https://fonts.googleapis.com/css2?family=Open+Sans:wght@400;700&display=swap" rel="stylesheet">
<style>
  :root {
    --backdrop: #242424;
    --card: #141414;
    --ink: #ffffff;
    --ink-soft: #e6e6e6;
    --rule: #d9d9d9;
  }
  * { box-sizing: border-box; margin: 0; padding: 0; }
  html, body { width: 1200px; height: 780px; overflow: hidden; }
  body {
    background: var(--backdrop);
    font-family: "Open Sans", Arial, sans-serif;
    color: var(--ink);
    display: flex;
    align-items: center;
    justify-content: center;
    gap: 40px;
  }
  .card {
    width: 560px;
    height: 320px;
    background: var(--card);
    border-radius: 22px;
    position: relative;
    box-shadow: 0 10px 30px rgba(0,0,0,.45);
  }
  /* brand lockup */
  .brand {
    display: flex;
    align-items: center;
    gap: 10px;
    font-size: 22px;
    font-weight: 400;
    letter-spacing: .06em;
    text-transform: uppercase;
    color: var(--ink);
  }
  .brand-dot {
    width: 14px; height: 14px;
    border: 1.5px solid var(--ink);
    border-radius: 50%;
    flex: none;
  }

  /* back of card: services */
  .card-back { padding: 34px 34px 0; }
  .card-back .brand { justify-content: center; font-size: 20px; }
  .services-heading {
    text-align: center;
    font-size: 12.5px;
    letter-spacing: .02em;
    margin: 36px 0 28px;
  }
  .services {
    display: flex;
    justify-content: space-between;
  }
  .service-list { list-style: none; font-size: 13px; line-height: 1.55; }
  .service-list li { display: flex; align-items: center; gap: 7px; }
  .service-list.right li { justify-content: flex-end; }
  .tick { width: 14px; height: 14px; flex: none; }

  /* front of card: contact */
  .card-front { display: flex; align-items: center; }
  .front-brand {
    width: 300px;
    display: flex;
    justify-content: center;
    padding-top: 40px;
  }
  .front-brand .brand { font-size: 19px; flex-direction: row; text-align: left; line-height: 1.2; }
  .divider {
    width: 1px;
    height: 150px;
    background: var(--rule);
  }
  .contact { padding-left: 26px; }
  .contact-name { font-size: 22px; font-weight: 700; line-height: 1.1; }
  .contact-company { font-size: 13px; color: var(--ink-soft); margin-top: 4px; }
  .contact-lines { list-style: none; margin-top: 22px; font-size: 14px; line-height: 1.65; }
  .contact-lines li { display: flex; align-items: center; gap: 8px; }
  .icon { width: 13px; height: 13px; flex: none; }
</style>
</head>
<body>

  <section class="card card-back" aria-label="Card back – services">
    <div class="brand"><span class="brand-dot"></span>Harborline Renovations</div>
    <p class="services-heading">OUR SERVICES ARE 100% GUARANTEED SPECIALIZING IN:</p>
    <div class="services">
      <ul class="service-list left">
        <li><svg class="tick" viewBox="0 0 14 14"><circle cx="7" cy="7" r="6" fill="none" stroke="currentColor" stroke-width="1.4"/><path d="M4 7.2l2.2 2.3L10.5 3.5" fill="none" stroke="currentColor" stroke-width="1.6"/></svg>Remodel: Kitchen &amp; Bath</li>
        <li><svg class="tick" viewBox="0 0 14 14"><circle cx="7" cy="7" r="6" fill="none" stroke="currentColor" stroke-width="1.4"/><path d="M4 7.2l2.2 2.3L10.5 3.5" fill="none" stroke="currentColor" stroke-width="1.6"/></svg>Painting: Interior &amp; Exterior</li>
        <li><svg class="tick" viewBox="0 0 14 14"><circle cx="7" cy="7" r="6" fill="none" stroke="currentColor" stroke-width="1.4"/><path d="M4 7.2l2.2 2.3L10.5 3.5" fill="none" stroke="currentColor" stroke-width="1.6"/></svg>Flooring: Carpect, Vinyl, Wood</li>
        <li><svg class="tick" viewBox="0 0 14 14"><circle cx="7" cy="7" r="6" fill="none" stroke="currentColor" stroke-width="1.4"/><path d="M4 7.2l2.2 2.3L10.5 3.5" fill="none" stroke="currentColor" stroke-width="1.6"/></svg>Window &amp; Door Replacement</li>
      </ul>
      <ul class="service-list right">
        <li>Plumbing: Repairs &amp; Upgrades<svg class="tick" viewBox="0 0 14 14"><circle cx="7" cy="7" r="6" fill="none" stroke="currentColor" stroke-width="1.4"/><path d="M4 7.2l2.2 2.3L10.5 3.5" fill="none" stroke="currentColor" stroke-width="1.6"/></svg></li>
        <li>Energy-Efficient Upgrades<svg class="tick" viewBox="0 0 14 14"><circle cx="7" cy="7" r="6" fill="none" stroke="currentColor" stroke-width="1.4"/><path d="M4 7.2l2.2 2.3L10.5 3.5" fill="none" stroke="currentColor" stroke-width="1.6"/></svg></li>
        <li>Deck &amp; Patio Construction<svg class="tick" viewBox="0 0 14 14"><circle cx="7" cy="7" r="6" fill="none" stroke="currentColor" stroke-width="1.4"/><path d="M4 7.2l2.2 2.3L10.5 3.5" fill="none" stroke="currentColor" stroke-width="1.6"/></svg></li>
        <li>Water &amp; Mold Damage<svg class="tick" viewBox="0 0 14 14"><circle cx="7" cy="7" r="6" fill="none" stroke="currentColor" stroke-width="1.4"/><path d="M4 7.2l2.2 2.3L10.5 3.5" fill="none" stroke="currentColor" stroke-width="1.6"/></svg></li>
        <li>Garage Renovation<svg class="tick" viewBox="0 0 14 14"><circle cx="7" cy="7" r="6" fill="none" stroke="currentColor" stroke-width="1.4"/><path d="M4 7.2l2.2 2.3L10.5 3.5" fill="none" stroke="currentColor" stroke-width="1.6"/></svg></li>
      </ul>
    </div>
  </section>

  <section class="card card-front" aria-label="Card front – contact">
    <div class="front-brand">
      <div class="brand"><span class="brand-dot"></span>Harborline<br>Renovations</div>
    </div>
    <div class="divider"></div>
    <div class="contact">
      <p class="contact-name">Martin Hollis</p>
      <p class="contact-company">Harborline Renovations Inc.</p>
      <ul class="contact-lines">
        <li><svg class="icon" viewBox="0 0 14 14"><path d="M3 1.5l2.2 2.4-1.2 1.6c.8 1.8 2.1 3.1 3.9 3.9l1.6-1.2 2.4 2.2-1.4 2C6 11.8 2.2 8 1 3z" fill="currentColor"/></svg>858-471-9063</li>
        <li><svg class="icon" viewBox="0 0 14 14"><circle cx="7" cy="7" r="6" fill="none" stroke="currentColor" stroke-width="1.3"/><ellipse cx="7" cy="7" rx="2.6" ry="6" fill="none" stroke="currentColor" stroke-width="1.1"/><path d="M1 7h12" stroke="currentColor" stroke-width="1.1"/></svg>www.brightoakbuilders.com</li>
      </ul>
    </div>
  </section>

</body>
</html>
```